Valtera Drones webdesign: Innovative Drones service company in agriculture

We need a new website according the following conditions:
• Main colour orange and current logo;
• Transparent – open – trustworthy – dynamic - personal;
• Use the smartness and overview characteristics of the crow (Valtera is Latin for crow);
• Accessible to multiple target groups and markets:
o So not too horticultural, too green;
• Use contradictions:
o Future versus nostalgia;
o Smartness crow versus precision hummingbird;
o Technology versus mechanical;
• Kestam 2.4 GTR as a style icon?
• Long pager website
Updates

Website menu o Home o Crop monitoring  Applications Growth | Stress | Development | Diseases  Markets Breeding | Young plant | Potplants | Cutflowers | Vegetables | Soft fruit  Customer cases o Technology Aerial data collection | Artificial intelligence | Free data sets o About Vision | Company | Partners | Team | Career o Contact o News&downloads Logo: www.valteradrones-example.com

Target Market(s)

agriculture: owners, crop managers
oil&gas: maintenance, quality control managers and purchase managers
logistics: ware house managers, purchase managers

Industry/Entity Type

Agribusiness

Number of Pages Required

2 page

Colors
f78f20

Requirements
Must have
• long pager website
downloads
LinkedIn
Should not have
• Not too 'green' because first impression of designers of agriculture/horticulture is using the green colour. But that is not necessary.

Keep in mind that the current logo will be updates: the circle will be more 'general' and less 'agri'. Also the green colors in the logo will be slightly darker to make it more powerful.

```html
<!DOCTYPE html>
<html lang="en">
<head>
<meta charset="utf-8">
<title>Valtera Drones</title>
<link href="https://fonts.googleapis.com/css2?family=Montserrat:wght@400;500;600;700&family=Open+Sans:wght@400;600&display=swap" rel="stylesheet">
<style>
:root{
  --orange:#f47f20;
  --orange-light:#f89a3c;
  --green:#7aa22c;
  --green-dark:#5f8a1e;
  --ink:#1c1c1c;
  --muted:#6a6a6a;
  --grey-bg:#f1f1f1;
  --white:#ffffff;
}
*{box-sizing:border-box;margin:0;padding:0}
html,body{width:1200px;height:4158px;overflow:hidden;background:var(--white)}
body{position:relative;font-family:"Open Sans",Arial,sans-serif;color:var(--ink)}
.abs{position:absolute}
h2,h3,.nav a,.btn{font-family:"Montserrat",Arial,sans-serif}
.section-title{position:absolute;left:0;width:1200px;text-align:center;font-size:29px;font-weight:700;letter-spacing:.3px}
.rule{position:absolute;left:572px;width:56px;height:4px;background:var(--green);border-radius:2px}

/* header */
.site-header{position:absolute;left:0;top:0;width:1200px;height:97px;background:var(--white)}
.brand{position:absolute;left:70px;top:20px;display:flex;align-items:center;gap:12px}
.brand-dot{width:56px;height:56px;border-radius:50%;background:var(--orange)}
.brand-text{display:flex;flex-direction:column;font-family:"Montserrat",sans-serif;font-weight:700;color:var(--orange);line-height:1}
.brand-name{font-size:30px;letter-spacing:.5px}
.brand-sub{font-size:12px;letter-spacing:12.5px;margin-top:4px}
.nav{position:absolute;top:40px;right:75px;display:flex;gap:36px}
.nav a{font-size:13.5px;font-weight:500;color:#333;text-decoration:none}
.nav a.active{color:var(--orange);font-weight:600}

/* hero */
.hero{position:absolute;left:0;top:97px;width:1200px;height:568px;overflow:hidden;background:linear-gradient(180deg,#c9d5cf 0%,#7a9a6a 25%,#3e6a2c 55%,#6a4a2e 100%)}
.hero-badge{position:absolute;left:667px;top:106px;width:404px;height:404px;border-radius:50%;background:rgba(244,127,32,.93);text-align:center;color:var(--white)}
.hero-badge .icon{width:56px;height:56px;border-radius:50%;background:var(--white);margin:68px auto 0}
.hero-badge h1{font-family:"Montserrat",sans-serif;font-size:30px;line-height:37px;margin-top:14px}
.hero-badge h1 .light{font-weight:400}
.hero-badge h1 .bold{font-weight:700}
.btn-outline{display:inline-block;margin-top:22px;width:180px;height:47px;border:2px solid var(--white);border-radius:24px;line-height:43px;font-family:"Montserrat",sans-serif;font-weight:600;font-size:15px;color:var(--white)}

/* cards */
.feature-card{position:absolute;top:812px;width:329px;height:289px;border:2px solid #f3b27a;text-align:center}
.feature-card svg{margin-top:34px}
.feature-card h3{font-size:19px;font-weight:700;margin-top:16px}
.feature-card p{font-size:13px;line-height:23px;color:var(--muted);margin:12px 22px 0}
.btn-pill{display:inline-block;margin-top:14px;width:161px;height:42px;border:2px solid var(--green);border-radius:22px;line-height:38px;font-family:"Montserrat",sans-serif;font-weight:600;font-size:13.5px;color:var(--green)}

/* about */
.about{position:absolute;left:0;top:1160px;width:1200px;height:471px;background:var(--grey-bg)}
.about-art{position:absolute;left:97px;top:43px;width:420px;height:396px;background:radial-gradient(ellipse at center,#9a9a9a 0%,#d8d8d8 55%,var(--grey-bg) 75%)}
.about h2{position:absolute;left:590px;top:85px;font-size:32px;font-weight:700;color:var(--orange)}
.about p{position:absolute;left:588px;top:152px;width:520px;font-size:15px;line-height:23.5px;color:#333}
.btn-solid{position:absolute;width:172px;height:46px;border-radius:23px;background:var(--green);color:var(--white);text-align:center;line-height:46px;font-family:"Montserrat",sans-serif;font-weight:600;font-size:15px}

/* technology */
.tech-band{position:absolute;left:0;top:1634px;width:1200px;height:390px;background:linear-gradient(180deg,#f07a1c 0%,#f58e30 60%,#ef7a1e 100%)}
.tech-title{color:var(--white)}
.tech-circle{position:absolute;top:1771px;width:372px;height:372px;border-radius:50%;text-align:center;color:var(--white);overflow:hidden}
.tech-circle.dark{background:radial-gradient(circle at 50% 45%,#5a5a5a 0%,#2a2a2a 70%,#1a1a1a 100%)}
.tech-circle.lead{background:radial-gradient(circle at 50% 45%,#8ab83a 0%,#74a62a 70%,#689a22 100%);box-shadow:0 12px 30px rgba(0,0,0,.25);z-index:2}
.tech-circle svg{margin-top:92px}
.tech-circle h3{font-size:21px;line-height:29px;font-weight:700;margin-top:12px}
.tech-circle p{font-size:13px;line-height:23px;margin:10px 60px 0;opacity:.95}

/* partners */
.partner{position:absolute;background:#9a9a9a}

/* news */
.news{position:absolute;left:0;top:2616px;width:1200px;height:622px;background:var(--grey-bg)}
.news-card{position:absolute;top:154px;width:294px;height:384px;background:var(--white)}
.news-card .photo{height:173px}
.news-card time{display:block;margin:22px 0 0 30px;font-family:"Montserrat",sans-serif;font-size:12px;font-weight:600;color:var(--green)}
.news-card h3{margin:14px 26px 0 30px;font-size:17px;line-height:20px;font-weight:500}
.news-card p{margin:12px 26px 0 30px;font-size:11.5px;line-height:18px;color:var(--muted)}
.news-card a{display:block;margin:10px 0 0 32px;font-family:"Montserrat",sans-serif;font-size:12px;font-weight:600;color:var(--orange);text-decoration:none}

/* contact */
.contact h2{position:absolute;left:132px;top:3343px;font-size:29px;font-weight:700}
.field{position:absolute;border:1px solid #9a9a9a;background:var(--white);font-size:15px;color:#333;padding:10px 17px}
.car-art{position:absolute;left:630px;top:3375px;width:557px;height:307px;border-radius:40px 60px 20px 20px;background:linear-gradient(180deg,#f07a3a 0%,#e55a20 60%,#cfd0d0 100%)}

/* footer */
.site-footer{position:absolute;left:0;top:3779px;width:1200px;height:379px;background:var(--orange);color:var(--white)}
.site-footer h4{position:absolute;top:72px;font-family:"Montserrat",sans-serif;font-size:19px;font-weight:600}
.site-footer ul{position:absolute;top:110px;list-style:none;font-size:14.5px;line-height:28.5px}
.contact-list li{display:flex;align-items:center;gap:10px}
.social{position:absolute;left:762px;top:215px;display:flex;gap:28px}
.social span{width:16px;height:16px;border-radius:50%;background:var(--white)}
.footer-rule{position:absolute;left:132px;top:310px;width:955px;height:1px;background:rgba(255,255,255,.35)}
.copyright{position:absolute;left:0;top:332px;width:1200px;text-align:center;font-size:14px}
</style>
</head>
<body>

<header class="site-header">
  <div class="brand"><span class="brand-dot"></span><span class="brand-text"><span class="brand-name">VALTERA</span><span class="brand-sub">DRONES</span></span></div>
  <nav class="nav">
    <a class="active">HOME</a><a>CROP MONITORING</a><a>TECHNOLOGY</a><a>ABOUT</a><a>CONTACT</a><a>NEWS &amp; DOWNLOADS</a>
  </nav>
</header>

<section class="hero" role="img" aria-label="Orange drone flying low over rows of flowering plants inside a greenhouse, with its flight path marked">
  <svg class="abs" style="left:0;top:0" width="1200" height="568" aria-hidden="true">
    <polyline points="62,250 46,266 62,282" stroke="#fff" stroke-width="5" fill="none"/>
    <polyline points="1160,250 1176,266 1160,282" stroke="#fff" stroke-width="5" fill="none"/>
  </svg>
  <div class="hero-badge">
    <div class="icon"></div>
    <h1><span class="light">ENABLES AERIAL</span><br><span class="bold">DATA-COLLECTION IN<br>GREENHOUSES</span></h1>
    <span class="btn-outline">LEARN MORE</span>
  </div>
</section>

<h2 class="section-title" style="top:727px">CROP MONITORING</h2>
<div class="rule" style="top:765px"></div>

<article class="feature-card" style="left:81px">
  <svg width="64" height="62" viewBox="0 0 64 62" fill="none" stroke="#f47f20" stroke-width="3"><rect x="4" y="4" width="56" height="40" rx="3"/><rect x="14" y="14" width="20" height="14"/><line x1="38" y1="16" x2="50" y2="16"/><line x1="38" y1="24" x2="50" y2="24"/><line x1="32" y1="44" x2="32" y2="54"/><line x1="20" y1="56" x2="44" y2="56"/></svg>
  <h3>APPLICATIONS</h3>
  <p>Augiat in pede Fusce tellus Sed metus augue convallis et vehicula ut pulvinar</p>
  <span class="btn-pill">LEARN MORE</span>
</article>
<article class="feature-card" style="left:428px">
  <svg width="92" height="62" viewBox="0 0 92 62" fill="none" stroke="#f47f20" stroke-width="3"><path d="M4 58 V34 A30 30 0 0 1 64 14 L82 30 V58 Z"/><path d="M18 58 V34 A16 16 0 0 1 50 34 V58"/><line x1="34" y1="6" x2="34" y2="58"/><line x1="4" y1="58" x2="82" y2="58"/></svg>
  <h3>MARKETS</h3>
  <p>Augiat in pede Fusce tellus Sed metus augue convallis et vehicula ut pulvinar</p>
  <span class="btn-pill">LEARN MORE</span>
</article>
<article class="feature-card" style="left:782px">
  <svg width="74" height="62" viewBox="0 0 74 62" fill="none" stroke="#f47f20" stroke-width="3"><circle cx="37" cy="12" r="8"/><circle cx="15" cy="20" r="7"/><circle cx="59" cy="20" r="7"/><path d="M25 58 V36 a12 12 0 0 1 24 0 V58 Z"/><path d="M4 58 V40 a11 11 0 0 1 20 -6"/><path d="M70 58 V40 a11 11 0 0 0 -20 -6"/></svg>
  <h3>CUSTOMER CASES</h3>
  <p>Augiat in pede Fusce tellus Sed metus augue convallis et vehicula ut pulvinar</p>
  <span class="btn-pill">LEARN MORE</span>
</article>

<section class="about">
  <div class="about-art" role="img" aria-label="Black ink sketch of a crow in flight"></div>
  <h2>ABOUT VALTERA DRONES</h2>
  <p>Valtera Drones has developed a unique autonomous drone system that is able to fly and navigate in a greenhouse without manual interference. Based on a flight plan the drone follows the right coordinates in the greenhouse, day or night, collecting high accurate data.<br>Data is being interpreted by Artificial Intelligence software resulting in crop improvement information. The focus is the following four customer pains: Development, Plant stress, Growth and Diseases.</p>
  <span class="btn-solid" style="left:585px;top:347px">LEARN MORE</span>
</section>

<div class="tech-band" role="img" aria-label="Orange tinted photo of a greenhouse interior"></div>
<h2 class="section-title tech-title" style="top:1686px">CROP MONITORING</h2>
<div class="rule" style="top:1726px;background:#fff"></div>

<article class="tech-circle dark" style="left:105px">
  <svg width="90" height="60" viewBox="0 0 90 60" fill="none" stroke="#fff" stroke-width="3"><line x1="6" y1="6" x2="34" y2="6"/><line x1="56" y1="6" x2="84" y2="6"/><line x1="20" y1="6" x2="32" y2="28"/><line x1="70" y1="6" x2="58" y2="28"/><rect x="30" y="24" width="30" height="16" rx="4"/><circle cx="45" cy="48" r="7"/></svg>
  <h3>AERIAL DATA<br>COLLECTION</h3>
  <p>Data is being interpreted by Artificial Intelligence software resulting</p>
</article>
<article class="tech-circle dark" style="left:762px">
  <svg width="70" height="64" viewBox="0 0 70 64" fill="none" stroke="#fff" stroke-width="3"><path d="M6 28 L35 6 L64 28"/><path d="M12 24 V60 H58 V24"/><path d="M24 60 V40 a11 11 0 0 1 22 0 V60"/><line x1="35" y1="30" x2="35" y2="60"/></svg>
  <h3>FREE DATA<br>SETS</h3>
  <p>Data is being interpreted by Artificial Intelligence software resulting</p>
</article>
<article class="tech-circle lead" style="left:428px">
  <svg width="70" height="64" viewBox="0 0 70 64" fill="none" stroke="#fff" stroke-width="3"><path d="M18 36 a12 12 0 0 1 4 -23 a15 15 0 0 1 28 2 a11 11 0 0 1 2 21 Z"/><rect x="26" y="18" width="18" height="16"/><line x1="35" y1="36" x2="35" y2="60"/><line x1="24" y1="44" x2="46" y2="44"/></svg>
  <h3>ARTIFICIAL<br>INTELLIGENCE</h3>
  <p>Data is being interpreted by Artificial Intelligence software resulting</p>
</article>

<h2 class="section-title" style="top:2203px">OUR PARTNERS</h2>
<div class="rule" style="top:2240px"></div>
<div class="partner" style="left:113px;top:2310px;width:114px;height:36px;border-radius:18px;background:#7a7a7a"></div>
<div class="partner" style="left:340px;top:2320px;width:100px;height:30px"></div>
<div class="partner" style="left:535px;top:2318px;width:148px;height:26px;background:#8a8a8a"></div>
<div class="partner" style="left:767px;top:2318px;width:26px;height:26px;background:#777"></div>
<div class="partner" style="left:983px;top:2316px;width:130px;height:30px;border-radius:15px;background:#b0b0b0"></div>
<div class="partner" style="left:130px;top:2420px;width:80px;height:80px;border-radius:50%;background:#8a8a8a"></div>
<div class="partner" style="left:338px;top:2428px;width:102px;height:62px;background:#8a8a8a"></div>
<div class="partner" style="left:549px;top:2440px;width:120px;height:34px;background:#8a8a8a"></div>
<div class="partner" style="left:765px;top:2430px;width:124px;height:50px;background:#b0b0b0"></div>
<div class="partner" style="left:990px;top:2436px;width:112px;height:40px;background:#8a8a8a"></div>

<section class="news">
  <h2 class="section-title" style="top:55px">LATEST NEWS</h2>
  <div class="rule" style="top:99px"></div>
  <article class="news-card" style="left:126px">
    <div class="photo" role="img" aria-label="Rows of orange gerbera flowers under greenhouse lights" style="background:linear-gradient(180deg,#7fb3e0 0%,#4a8a3a 60%,#e86a22 100%)"></div>
    <time>JAN 20, 2020</time>
    <h3>Curabitur iaculis tempus eros Curabitur vel</h3>
    <p>Curabitur vel dolor ultrices ipsum dictum tristique Praesent vitae lacus Ut velit enim vestibulum non fermentum</p>
    <a>LEARN MORE ›</a>
  </article>
  <article class="news-card" style="left:459px">
    <div class="photo" role="img" aria-label="Orange drone hovering above green crop beds" style="background:linear-gradient(180deg,#8a9a90 0%,#5a7a4a 45%,#3f7a2e 100%)"></div>
    <time>JAN 15, 2020</time>
    <h3>Nunc tempus felis vitae urna Vivamus</h3>
    <p>Curabitur vel dolor ultrices ipsum dictum tristique Praesent vitae lacus Ut velit enim vestibulum non fermentum</p>
    <a>LEARN MORE ›</a>
  </article>
  <article class="news-card" style="left:791px">
    <div class="photo" role="img" aria-label="Delivery drones above lettuce rows in a greenhouse" style="background:linear-gradient(180deg,#e6ecec 0%,#9ac07a 55%,#4f8a2e 100%)"></div>
    <time>JAN 10, 2020</time>
    <h3>Praesent sit amet est In dictum dolor eu dictu</h3>
    <p>Curabitur vel dolor ultrices ipsum dictum tristique Praesent vitae lacus Ut velit enim vestibulum non fermentum</p>
    <a>LEARN MORE ›</a>
  </article>
</section>

<section class="contact">
  <h2>CONTACT US</h2>
  <div class="rule" style="left:132px;top:3386px"></div>
  <div class="field" style="left:132px;top:3417px;width:231px;height:46px">First Name</div>
  <div class="field" style="left:373px;top:3417px;width:233px;height:46px">Last Name</div>
  <div class="field" style="left:132px;top:3472px;width:231px;height:46px">Email address</div>
  <div class="field" style="left:373px;top:3472px;width:233px;height:46px">Phone</div>
  <div class="field" style="left:132px;top:3527px;width:474px;height:96px">Message</div>
  <span class="btn-solid" style="left:124px;top:3645px;height:46px">SUBMIT</span>
  <div class="car-art" role="img" aria-label="Classic orange Kestam 2.4 GTR coupe, front three-quarter view"></div>
</section>

<footer class="site-footer">
  <h4 style="left:132px">COMPANY</h4>
  <ul style="left:134px"><li>Home</li><li>Technology</li><li>About</li><li>Vision</li></ul>
  <h4 style="left:302px">CROP MONITORING</h4>
  <ul style="left:304px"><li>Applications</li><li>Markets</li><li>Customer cases</li></ul>
  <h4 style="left:566px">RESOURCES</h4>
  <ul style="left:567px"><li>News</li><li>Downloads</li><li>Contact Us</li></ul>
  <h4 style="left:759px">CONTACT US</h4>
  <ul class="contact-list" style="left:762px">
    <li><svg width="14" height="16" viewBox="0 0 14 16"><path d="M7 0a6 6 0 0 0-6 6c0 4 6 10 6 10s6-6 6-10a6 6 0 0 0-6-6z" fill="#fff"/><circle cx="7" cy="6" r="2.2" fill="#f47f20"/></svg>Veldstraat 12B, 1234AB, Hoogland</li>
    <li><svg width="14" height="14" viewBox="0 0 14 14"><path d="M3 1l3 3-2 2c1 2 2 3 4 4l2-2 3 3-2 2C6 13 1 8 1 3z" fill="#fff"/></svg>Email: info@valteradrones-example.com</li>
    <li><svg width="16" height="12" viewBox="0 0 16 12"><rect width="16" height="12" fill="#fff"/><polyline points="0,0 8,7 16,0" fill="none" stroke="#f47f20" stroke-width="1.5"/></svg>Telephone: +31 6 12345678</li>
  </ul>
  <div class="social"><span></span><span></span><span></span></div>
  <div class="footer-rule"></div>
  <p class="copyright">© 2020 Company Name | All Rights Reserved</p>
</footer>

</body>
</html>
```